Business card design needed

Need a new business card design for a new business in Sydney, Australia called 'Verrowin Australia'. The business deals in consulting for new sales, sales leadership and customer service consultancy. Want the business card to look professional and clean

Industry/Entity Type

Leadership

Contact Information for Business Card

Verrowin Australia
Tobias Wrenley
Managing Director

14 Quarrion Avenue
Marrowdale NSW 2041

0432 517 806
tobias@verrowin.com.au
www.verrowin.com.au

```html
<!DOCTYPE html>
<html lang="en">
<head>
<meta charset="utf-8">
<title>Verrowin Australia – Business Card</title>
<link href="https://fonts.googleapis.com/css2?family=Arimo:wght@400;700&display=swap" rel="stylesheet">
<style>
  :root {
    --paper: #ffffff;
    --ink: #1a1a1a;
    --accent-red: #e8301c;
    --accent-blue: #1f2f9c;
    --accent-grey: #6f7675;
  }
  * { margin: 0; padding: 0; box-sizing: border-box; }
  html, body {
    width: 1200px;
    height: 741px;
    overflow: hidden;
    background: var(--paper);
  }
  .business-card {
    position: relative;
    width: 1200px;
    height: 741px;
    background: var(--paper);
    font-family: "Arimo", Arial, sans-serif;
    color: var(--ink);
  }
  .website {
    position: absolute;
    left: 60px;
    top: 58px;
    font-size: 25px;
    font-weight: 700;
    letter-spacing: 0.02em;
  }
  .contact-person {
    position: absolute;
    right: 60px;
    top: 40px;
    text-align: right;
    font-size: 30px;
    letter-spacing: 0.12em;
    line-height: 1.25;
  }
  .contact-person .person-name { font-weight: 700; }
  .contact-person .person-role { color: var(--accent-red); font-weight: 400; }

  .brand {
    position: absolute;
    left: 330px;
    top: 230px;
    display: flex;
    align-items: center;
    gap: 34px;
  }
  .brand-dot {
    width: 96px;
    height: 96px;
    flex: none;
  }
  .brand-name {
    font-size: 96px;
    font-weight: 700;
    line-height: 0.95;
    letter-spacing: -0.02em;
    color: var(--ink);
  }

  .address-line {
    position: absolute;
    left: 118px;
    top: 656px;
    font-size: 25px;
    font-weight: 700;
    letter-spacing: 0.01em;
    white-space: nowrap;
  }
</style>
</head>
<body>
  <main class="business-card">
    <p class="website">www.verrowin.com.au</p>

    <div class="contact-person">
      <p class="person-name">Tobias Wrenley</p>
      <p class="person-role">Managing Director</p>
    </div>

    <div class="brand">
      <svg class="brand-dot" viewBox="0 0 96 96" aria-hidden="true">
        <circle cx="48" cy="48" r="48" fill="var(--accent-blue)"/>
      </svg>
      <p class="brand-name">Verrowin<br>Australia</p>
    </div>

    <p class="address-line">14 Quarrion Avenue Marrowdale NSW 2041 0432 517 806 tobias@verrowin.com.au</p>
  </main>
</body>
</html>
```